Corporate brochure design 4 pages

Hi,

We are a real estate company based in Europe.

We have almost finalized a rebranding.

We are developing a brand book guidelines (still on working process) to help you undertstand the look and feel of our new CI. I would like to receive proposals of design for a corporate brochure template. I need to receive the Indesign files with full ownership rights to be able to adapt all our documentation with this template.
Regarding the images, you can take gabaris on www.pelvaromedia.com. I will be able to take them afterwards.

There will be 4 pages. you will receive the 4 pages on pdf for your consideration with our (almost) actual layout.

- 1st page: cover
- 2nd page: company presentation in french and english
- 3rd page: some market data + graph
- 4th page: 2 retail centers presentation.

In the template, i need to have:
- the paragraph styles in order
- 2 different masters with top/bottom/page number aso.

Please feel free to ask any other questions.

best regards,
Updates

I would like to precise tha t we are active on the commercial real estate sector:

- office transactions (rent /sales)
- property management of administrative and business buildings
- Valuation of properties
- Capital markets (investment advices for selling building)

Industry/Entity Type

Real Estate

Colors

Designer to choose colors to be used in the design.

```html
<!DOCTYPE html>
<html lang="fr">
<head>
<meta charset="utf-8">
<title>Luxembourg Office Market Report Q3-2013</title>
<link href="https://fonts.googleapis.com/css2?family=Montserrat:wght@400;500;700&family=Arimo:wght@400;700&display=swap" rel="stylesheet">
<style>
:root{
  --stage:#2b2826;
  --paper:#ffffff;
  --ink:#1e1e1e;
  --grey:#555555;
  --muted:#8a8a8a;
  --rule:#d6d6d6;
  --orange:#f26522;
  --orange-light:#f7904f;
  --photo-warm-a:#d9c3a4;
  --photo-warm-b:#9a6a3e;
  --photo-cool-a:#dde6ea;
  --photo-cool-b:#7e9099;
}
*{margin:0;padding:0;box-sizing:border-box}
html,body{width:1200px;height:750px;overflow:hidden;background:var(--stage)}
.spread{position:relative;width:1200px;height:750px}
.page{position:absolute;top:138px;width:548px;height:545px;background:var(--paper);overflow:hidden}
.page--left{left:51px}
.page--right{left:600px;width:545px}
.abs{position:absolute}
.report-title{font-family:"Montserrat",sans-serif;font-size:10.5px;line-height:12.5px;font-weight:400;letter-spacing:.2px;color:var(--grey);text-transform:uppercase}
.report-title--en{color:var(--orange)}
.section-label{display:block;font-family:"Montserrat",sans-serif;font-weight:700;font-size:6.5px;line-height:9px;color:var(--ink);letter-spacing:.2px}
.report-title--en .section-label{color:var(--orange)}
.body-copy{font-family:"Arimo",sans-serif;font-size:6.6px;line-height:10.4px;color:var(--ink);text-align:justify}
.body-copy--en{color:var(--orange)}
.body-copy strong{font-weight:700}
.aside{font-family:"Montserrat",sans-serif;font-size:7.4px;line-height:10.2px;color:var(--grey);text-transform:uppercase}
.aside--en{color:var(--orange)}
.aside-rule{height:1px;background:var(--rule)}
.photo{position:absolute}
.photo--office{left:113px;top:299px;width:412px;height:223px;background:linear-gradient(180deg,var(--photo-cool-a) 0%,#c9c3b6 45%,var(--photo-warm-a) 62%,var(--photo-warm-b) 100%)}
.photo--meeting{left:316px;top:154px;width:229px;height:138px;background:linear-gradient(160deg,#f3f5f6 0%,var(--photo-cool-a) 40%,var(--photo-cool-b) 100%)}
.folio{font-family:"Montserrat",sans-serif;font-size:5px;line-height:7px;color:var(--orange);text-align:right}
.folio span{display:block;color:var(--muted)}
.stock-table{position:absolute;left:24px;top:155px;width:261px;font-family:"Arimo",sans-serif;font-size:6.6px;color:var(--grey)}
.rule{height:1px;background:var(--rule)}
.rule--orange{background:var(--orange-light)}
.row{display:flex;height:10.4px;line-height:10.4px}
.col-area{width:84px;font-family:"Montserrat",sans-serif;font-weight:700;font-size:6.3px;color:var(--orange);line-height:10.4px}
.col-district{width:75px}
.col-m2{width:60px;text-align:right}
.col-pct{flex:1;text-align:right}
.row--head{height:15px;line-height:15px;font-family:"Montserrat",sans-serif;font-weight:700;font-size:6px;color:var(--ink)}
.row--total{font-family:"Montserrat",sans-serif;font-weight:700;font-size:6px;color:var(--ink);margin-top:7px}
.group{padding:6px 0 10px}
.row--grand{font-family:"Montserrat",sans-serif;font-weight:700;font-size:6.3px;color:var(--orange);height:14px;line-height:14px}
.graph-title{position:absolute;left:316px;top:310px;font-family:"Montserrat",sans-serif;font-weight:700;font-size:6.5px;line-height:11px;color:var(--ink)}
.graph-title span{display:block;color:var(--orange)}
.chart{position:absolute;left:310px;top:340px}
.chart text{font-family:"Montserrat",sans-serif}
</style>
</head>
<body>
<main class="spread">

  <section class="page page--left">
    <h1 class="report-title abs" style="left:114px;top:25px">Rapport de marché bureaux<br>Luxembourg Q3-2013<span class="section-label">INTRODUCTION</span></h1>
    <h2 class="report-title report-title--en abs" style="left:326px;top:25px">Luxembourg office market<br>report Q3-2013<span class="section-label">INTRODUCTION</span></h2>

    <p class="body-copy abs" style="left:114px;top:89px;width:200px">Lorem ipsum dolor sit amet, consectetuer adipiscing elit. Duis pulvinar lectus. Fusce lacinia. Cras massa tortor, dignissim eu, sollicitudin eu, consequat et, magna. Proin tempor. Mauris leo orci, pretium at, pharetra a, egestas id, ligula. Morbi non magna. Nunc auctor nibh ac justo. Quisque egestas imperdiet risus. Nunc nibh ligula, imperdiet non, feugiat eu, commodo quis, justo. In hac habitasse platea dictumst. Aliquam in enim. Donec dignissim metus ac purus. Aliquam sed mi non diam molestie posuere. Lorem ipsum dolor sit amet, consectetuer adipiscing elit.</p>
    <p class="body-copy body-copy--en abs" style="left:326px;top:89px;width:200px">Lorem ipsum dolor sit amet, consectetuer adipiscing elit. Duis pulvinar lectus. Fusce lacinia. Cras massa tortor, dignissim eu, sollicitudin eu, consequat et, magna. Proin tempor. Mauris leo orci, pretium at, pharetra a, egestas id, ligula. Morbi non magna. Nunc auctor nibh ac justo. Quisque egestas imperdiet risus. Nunc nibh ligula, imperdiet non, feugiat eu, commodo quis, justo. In hac habitasse platea dictumst. Aliquam in enim. Donec dignissim metus ac purus. Aliquam sed mi non diam molestie posuere. Lorem ipsum dolor sit amet, consectetuer adipiscing elit.</p>

    <div class="aside-rule abs" style="left:27px;top:203px;width:290px"></div>
    <p class="aside abs" style="left:27px;top:194px;width:80px">Aliquam erat et volutpat. In faucibus volut ipsum.</p>
    <p class="aside aside--en abs" style="left:27px;top:246px;width:80px">Aliquam erat et volutpat. In faucibus volutp ipsum.</p>

    <p class="body-copy abs" style="left:114px;top:194px;width:200px"><strong>Fusce velit. Phasellus cursus.</strong> Lorem ipsum dolor sit amet, consectetuer adipiscing elit. In pretium nulla id velit. Morbi convallis neque quis magna. Duis pede. Aliquam erat volutpat. In faucibus volutpat ipsum. Mauris in neque. Nunc laoreet. Cras eu ipsum vel sapien congue sollicitudin. Sed gravida ante non nulla. Pellentesque id wisi eget ante auctor imperdiet. Pellentesque ornare lectus ac orci. In iaculis justo sed sem. Praesent porttitor, ipsum semper accumsan varius, lacus leo vulputate erat, in pretium dui metus gravida arcu. Vivamus quis wisi. Aliquam erat volutpat.</p>
    <p class="body-copy body-copy--en abs" style="left:326px;top:194px;width:200px"><strong>Fusce velit. Phasellus cursus.</strong> Lorem ipsum dolor sit amet, consectetuer adipiscing elit. In pretium nulla id velit. Morbi convallis neque quis magna. Duis pede. Aliquam erat volutpat. In faucibus volutpat ipsum. Mauris in neque. Nunc laoreet. Cras eu ipsum vel sapien congue sollicitudin. Sed gravida ante non nulla. Pellentesque id wisi eget ante auctor imperdiet. Pellentesque ornare lectus ac orci. In iaculis justo sed sem. Praesent porttitor, ipsum semper accumsan varius, lacus leo vulputate erat, in pretium dui metus gravida arcu. Vivamus quis wisi. Aliquam erat volutpat.</p>

    <div class="photo photo--office" role="img" aria-label="Photo: bright open-plan office lobby with wooden floor and people walking"></div>
  </section>

  <section class="page page--right">
    <h2 class="report-title abs" style="left:24px;top:25px">Rapport de marché bureaux<br>Luxembourg Q3-2013<span class="section-label">STOCK</span></h2>
    <h2 class="report-title report-title--en abs" style="left:235px;top:25px">Luxembourg office market<br>report Q3-2013<span class="section-label">STOCK</span></h2>
    <div class="folio abs" style="left:505px;top:19px;width:20px">04<span>05</span></div>

    <p class="body-copy abs" style="left:24px;top:89px;width:200px;text-align:left">Le stock de mètres carrés disponibles de bureaux a augmenté de 0,36 % au troisième trimestre de cette année grâce à la livraison de près de 12 300 m². Le stock total équivaut à 3 465 600 m².</p>
    <p class="body-copy body-copy--en abs" style="left:235px;top:89px;width:200px;text-align:left">The stock of available office square meters has increased by 0,36% during the third quarter of this year with the delivery of 12,300 m². The total stock reaches 3,465,600 m².</p>

    <div class="stock-table">
      <div class="rule rule--orange"></div>
      <div class="row row--head"><span class="col-area"></span><span class="col-district">QUARTIERS-DISTRICTS</span><span class="col-m2">STOCK M²</span><span class="col-pct">STOCK %</span></div>
      <div class="rule rule--orange"></div>

      <div class="group">
        <div class="row"><span class="col-area">CENTRE-VILLE</span><span class="col-district">Kirchberg</span><span class="col-m2">915 000</span><span class="col-pct">26,42</span></div>
        <div class="row"><span class="col-area">(CITY)</span><span class="col-district">CBD</span><span class="col-m2">806 400</span><span class="col-pct">23,27</span></div>
        <div class="row"><span class="col-area"></span><span class="col-district">Station</span><span class="col-m2">382 700</span><span class="col-pct">11,04</span></div>
        <div class="row"><span class="col-area"></span><span class="col-district">Cloche d'Or</span><span class="col-m2">365 600</span><span class="col-pct">10,55</span></div>
        <div class="row"><span class="col-area"></span><span class="col-district">Limpertsberg</span><span class="col-m2">85 000</span><span class="col-pct">2,45</span></div>
        <div class="row"><span class="col-area"></span><span class="col-district">Belair/Merl</span><span class="col-m2">67 800</span><span class="col-pct">1,96</span></div>
        <div class="row"><span class="col-area"></span><span class="col-district">Hamm</span><span class="col-m2">44 500</span><span class="col-pct">1,28</span></div>
        <div class="row"><span class="col-area"></span><span class="col-district">Kalchesbrück</span><span class="col-m2">33 000</span><span class="col-pct">0,95</span></div>
        <div class="row row--total"><span class="col-area"></span><span class="col-district">TOTAL</span><span class="col-m2">2 700 500</span><span class="col-pct">77,92</span></div>
      </div>
      <div class="rule"></div>

      <div class="group" style="padding-top:9px">
        <div class="row"><span class="col-area">VILLE-PÉRIPHÉRIE</span><span class="col-district">Airport - Findel</span><span class="col-m2">157 500</span><span class="col-pct">4,54</span></div>
        <div class="row"><span class="col-area">(CITY-PERIPHERY)</span><span class="col-district">Bertrange/Bourmicht</span><span class="col-m2">82 000</span><span class="col-pct">2,37</span></div>
        <div class="row"><span class="col-area"></span><span class="col-district">Strassen</span><span class="col-m2">81 050</span><span class="col-pct">2,34</span></div>
        <div class="row"><span class="col-area"></span><span class="col-district">Howald</span><span class="col-m2">62 600</span><span class="col-pct">1,81</span></div>
        <div class="row row--total"><span class="col-area"></span><span class="col-district">TOTAL</span><span class="col-m2">383 150</span><span class="col-pct">11,06</span></div>
      </div>
      <div class="rule"></div>

      <div class="group" style="padding-top:9px">
        <div class="row"><span class="col-area">PÉRIPHÉRIE</span><span class="col-district">Belval</span><span class="col-m2">93 090</span><span class="col-pct">2,69</span></div>
        <div class="row"><span class="col-area">(PERIPHERY)</span><span class="col-district">Capellen</span><span class="col-m2">69 500</span><span class="col-pct">2,01</span></div>
        <div class="row"><span class="col-area"></span><span class="col-district">Leudelange</span><span class="col-m2">73 556</span><span class="col-pct">2,12</span></div>
        <div class="row"><span class="col-area"></span><span class="col-district">Munsbach</span><span class="col-m2">60 100</span><span class="col-pct">1,73</span></div>
        <div class="row"><span class="col-area"></span><span class="col-district">Windhof</span><span class="col-m2">40 600</span><span class="col-pct">1,17</span></div>
        <div class="row"><span class="col-area"></span><span class="col-district">Esch-sur-Alzette</span><span class="col-m2">24 700</span><span class="col-pct">0,71</span></div>
        <div class="row"><span class="col-area"></span><span class="col-district">Contern</span><span class="col-m2">20 400</span><span class="col-pct">0,59</span></div>
        <div class="row row--total"><span class="col-area"></span><span class="col-district">TOTAL</span><span class="col-m2">381 946</span><span class="col-pct">11,02</span></div>
      </div>
      <div class="rule rule--orange"></div>
      <div class="row row--grand"><span class="col-area">TOTAL</span><span class="col-district"></span><span class="col-m2">3 465 596</span><span class="col-pct"></span></div>
      <div class="rule rule--orange"></div>
    </div>

    <div class="photo photo--meeting" role="img" aria-label="Photo: meeting room with glass table and black office chairs"></div>

    <p class="graph-title">GRAPHIQUE TITRE<span>GRAPH TITLE</span></p>

    <svg class="chart" width="220" height="170" viewBox="0 0 220 170" aria-label="Office stock 2003–2013 bar chart">
      <g font-size="5" font-weight="700" fill="#1e1e1e">
        <text transform="translate(36,18) rotate(-45)">1.700</text>
        <text transform="translate(61,18) rotate(-45)">2.000</text>
        <text transform="translate(86,18) rotate(-45)">2.300</text>
        <text transform="translate(111,18) rotate(-45)">2.600</text>
        <text transform="translate(136,18) rotate(-45)">2.900</text>
        <text transform="translate(161,18) rotate(-45)">3.200</text>
        <text transform="translate(186,18) rotate(-45)">3.500</text>
      </g>
      <g stroke="#f26522" stroke-width=".6" fill="none">
        <path d="M36 20V33"/><path d="M61 20V44"/><path d="M86 20V55"/><path d="M111 20V66"/>
        <path d="M136 20V77"/><path d="M161 20V99"/><path d="M186 20V121"/>
      </g>
      <g font-size="4.6" fill="#8a8a8a">
        <text x="0" y="39">2013</text><text x="0" y="50">2012</text><text x="0" y="61">2011</text>
        <text x="0" y="72">2010</text><text x="0" y="83">2009</text><text x="0" y="94">2008</text>
        <text x="0" y="105">2007</text><text x="0" y="116">2006</text><text x="0" y="127">2005</text>
        <text x="0" y="138">2004</text><text x="0" y="149">2003</text>
      </g>
      <g>
        <rect x="21" y="33" width="44" height="10" fill="#f26522"/>
        <rect x="21" y="44" width="53" height="10" fill="#f7904f"/>
        <rect x="21" y="55" width="63" height="10" fill="#f26522"/>
        <rect x="21" y="66" width="75" height="10" fill="#f7904f"/>
        <rect x="21" y="77" width="88" height="10" fill="#f26522"/>
        <rect x="21" y="88" width="98" height="10" fill="#f7904f"/>
        <rect x="21" y="99" width="120" height="10" fill="#f26522"/>
        <rect x="21" y="110" width="125" height="10" fill="#f7904f"/>
        <rect x="21" y="121" width="138" height="10" fill="#f26522"/>
        <rect x="21" y="132" width="141" height="10" fill="#f7904f"/>
        <rect x="21" y="143" width="145" height="10" fill="#f26522"/>
      </g>
      <g font-size="4.6" font-weight="700" fill="#ffffff">
        <text x="24" y="39.7">3.211</text><text x="24" y="50.7">2.409</text><text x="24" y="61.7">2.502</text>
        <text x="24" y="72.7">2.600</text><text x="24" y="83.7">2.770</text><text x="24" y="94.7">2.912</text>
        <text x="24" y="105.7">3.170</text><text x="24" y="116.7">3.225</text><text x="24" y="127.7">3.325</text>
        <text x="24" y="138.7">3.406</text><text x="24" y="149.7">3.465</text>
      </g>
      <text x="158" y="59" font-size="4.8" font-weight="700" fill="#1e1e1e">Stock</text>
      <rect x="180" y="52" width="11" height="11" fill="#f26522"/>
    </svg>
  </section>

</main>
</body>
</html>
```